Sunny Paths and joy Business card

I have a logo, but will like a business card design. Is for a travel agency in Mexico. We focus in family experiences.

I will liek some thing different and unique, from the traditional business card, something to get remmeber for.

Business card information:

Leandro T. Ocampo
leandro@sunnypathsjoy.example

Alameda 482, 3 piso
Col. Tlalpizco
Mexico, D.F. 07320

office: (55) 5000-0142
mobile: (55) 9000-0187

www.sunnypathsjoy.example
@sunnypjoy
blog: sunnypathsandjoy.blogsite.example
facebook: SunnyPathsAndJoy

```html
<!DOCTYPE html>
<html lang="es">
<head>
<meta charset="utf-8">
<title>Sunny Paths and joy — Business Card</title>
<link rel="stylesheet" href="https://fonts.googleapis.com/css2?family=Chango&family=Sniglet:wght@800&family=Encode+Sans+Condensed:wght@700&family=Roboto+Condensed:ital,wght@1,700&display=swap">
<style>
  :root {
    --page: #ffffff;
    --card-edge: #5a6b72;
    --glow: #b8dc7e;
    --teal: #4ab3bf;
    --teal-deep: #3aa8b8;
    --brand-ink: #1d3f8c;
    --brand-dot: #e8f4f6;
    --contact-green: #1f8a3c;
    --contact-outline: #ffffff;
    --name-fill: #fff3a8;
    --name-inner: #e2461e;
    --name-outer: #ffe02a;
    --rule: #e0662a;
    --social-ink: #fff9c6;
    --social-shadow: rgba(60, 70, 30, 0.55);
    --band: #6b5fa0;
    --band-edge: #3f3560;
    --address-fill: #d8261e;
    --address-outline: #fff6c2;
  }
  * { margin: 0; padding: 0; box-sizing: border-box; }
  html, body {
    width: 1200px; height: 748px; overflow: hidden;
    background: var(--page);
  }
  .card {
    position: absolute;
    left: 18px; top: 33px; width: 1180px; height: 707px;
    border: 1px solid var(--card-edge);
    background: radial-gradient(ellipse 62% 70% at 50% 48%, var(--glow) 0%, #8fcf9a 45%, var(--teal) 80%, var(--teal-deep) 100%);
    overflow: hidden;
  }
  .brand {
    position: absolute; left: 14px; top: 40px; width: 300px; height: 270px;
    display: flex; align-items: center; gap: 14px;
  }
  .brand-dot {
    flex: 0 0 64px; height: 64px; border-radius: 50%;
    background: var(--brand-dot);
  }
  .brand-name {
    font-family: "Chango", serif; font-size: 32px; line-height: 1.1;
    color: var(--brand-ink);
  }
  .contact {
    position: absolute; left: 618px; top: 22px; width: 524px;
    font-family: "Sniglet", cursive; font-weight: 800; font-size: 28px;
    line-height: 45px; letter-spacing: 0.5px;
    color: var(--contact-green);
    -webkit-text-stroke: 1px var(--contact-outline);
    text-shadow: 0 0 2px var(--contact-outline), 0 0 2px var(--contact-outline);
    list-style: none; white-space: nowrap;
  }
  .person {
    position: absolute; left: 300px; top: 238px; width: 870px; height: 100px;
  }
  .person text {
    font-family: "Chango", serif; font-size: 58px;
  }
  .person .ghost { fill: rgba(255,255,255,0.45); filter: blur(4px); }
  .person .outer { fill: none; stroke: var(--name-outer); stroke-width: 16; stroke-linejoin: round; }
  .person .inner { fill: none; stroke: var(--name-inner); stroke-width: 7; stroke-linejoin: round; }
  .person .core { fill: var(--name-fill); }
  .rule {
    position: absolute; left: 309px; top: 347px; width: 845px; height: 3px;
    background: var(--rule);
  }
  .social {
    position: absolute; left: 42px; top: 361px;
    font-family: "Encode Sans Condensed", sans-serif; font-weight: 700;
    font-size: 40px; line-height: 80px;
    color: var(--social-ink);
    text-shadow: 1px 2px 3px var(--social-shadow);
    list-style: none; white-space: nowrap;
  }
  .address-band {
    position: absolute; left: 21px; top: 597px; width: 1129px; height: 80px;
    border-radius: 14px;
    background: var(--band);
    border: 1px solid var(--band-edge);
    display: flex; align-items: center; padding-left: 16px;
  }
  .address {
    font-family: "Roboto Condensed", sans-serif; font-style: italic; font-weight: 700;
    font-size: 48px; white-space: nowrap;
    color: var(--address-fill);
    -webkit-text-stroke: 1px var(--address-outline);
    text-shadow: 0 0 3px var(--address-outline), 0 0 3px var(--address-outline), 0 0 3px var(--address-outline);
  }
</style>
</head>
<body>
  <main class="card">
    <div class="brand">
      <span class="brand-dot"></span>
      <span class="brand-name">Sunny Paths and joy</span>
    </div>

    <ul class="contact">
      <li>Office: (55) 5000-0142</li>
      <li>Mobile: (55) 9000-0187</li>
      <li>www.sunnypathsjoy.example</li>
    </ul>

    <svg class="person" viewBox="0 0 870 100" aria-label="Leandro T. Ocampo">
      <text class="ghost" x="10" y="28">Leandro T. Ocampo</text>
      <text class="outer" x="10" y="78">Leandro T. Ocampo</text>
      <text class="inner" x="10" y="78">Leandro T. Ocampo</text>
      <text class="core" x="10" y="78">Leandro T. Ocampo</text>
    </svg>
    <div class="rule"></div>

    <ul class="social">
      <li>leandro@sunnypathsjoy.example</li>
      <li>facebook: SunnyPathsAndJoy · @sunnypjoy</li>
      <li>blog: sunnypathsandjoy.blogsite.example</li>
    </ul>

    <div class="address-band">
      <p class="address">Alameda 482, 3 piso Col. Tlalpizco Mexico, D.F. 07320</p>
    </div>
  </main>
</body>
</html>
```